Registry Program Flyer design 2 - MX Bridge registry

We need two different flyers that will be distributed via web, email and print. This project is for the second of the two flyers.

The audience is patients and family members of patients with a specific disease. The flyer will be used to make patients aware of our web-based registry programs, and to inform/encourage patients to join.

An example prototype flyer with the text that should be used is attached. We would like to improve the design and layout of the flyer, while retaining as much of the language as appropriate.

The MXBridge flyer should use the logo provided in the example and a color scheme compatible with the logo. The flyer may use the pictures included in the prototype.

If possible, a final format that allows us to edit the text is preferred. If this is not possible, we will finalize the text after receiving a prototype. Changes to the text will likely be minor.

Note: The design of the flyers for this project and the other project (Registry Program Flyer Design 1 - RTQV registry) can be similar in style, however, they should not be duplicates.

Deliverables will be a final .PSD (photoshop) file with layers so we can edit text if necessary.

Target Market(s)

Physicians and healthcare professionals.

Requirements
Must have
• Use the attached logo and colors.

```html
<!DOCTYPE html>
<html lang="en">
<head>
<meta charset="utf-8">
<title>MX Bridge Registry Flyer</title>
<link href="https://fonts.googleapis.com/css2?family=Arimo:wght@400;700&family=Arvo:wght@700&family=Changa+One&family=Lato:wght@400&display=swap" rel="stylesheet">
<style>
  :root {
    --frame-red: #a3141b;
    --frame-grey: #9ea5aa;
    --plum-dark: #4e1640;
    --plum: #7c2763;
    --orchid: #b94c9e;
    --ink: #1f1c22;
    --headline-red: #e3202b;
    --headline-shadow: #3a1020;
    --text: #232323;
    --white: #ffffff;
  }
  * { box-sizing: border-box; margin: 0; padding: 0; }
  html, body { width: 934px; height: 1200px; overflow: hidden; background: var(--white); }
  .flyer {
    position: relative; width: 934px; height: 1200px;
    background: var(--frame-red); padding: 13px;
    font-family: "Arimo", Arial, sans-serif; color: var(--text);
  }
  .flyer__inner {
    position: relative; width: 100%; height: 100%;
    background: var(--frame-grey); padding: 14px;
  }
  .flyer__sheet { position: absolute; left: 27px; top: 27px; width: 880px; height: 1146px; background: var(--white); overflow: hidden; }
  .sheet-abs { position: absolute; }
  .hero-photo {
    left: 0; top: 0; width: 880px; height: 600px;
    background: linear-gradient(180deg, #c9d2d8 0%, #aeb9bf 22%, #8f918c 38%, #b9aa98 55%, #d2c5b3 80%, #cbbca8 100%);
  }
  .chevron { left: 0; top: 0; width: 880px; height: 620px; }
  .brand-banner { left: 467px; top: 19px; width: 387px; height: 178px; }
  .brand-banner__name {
    position: absolute; left: 70px; top: 50px;
    font-family: "Lato", Arial, sans-serif; font-size: 38px; color: var(--ink); line-height: 1;
  }
  .brand-banner__dot { position: absolute; left: 24px; top: 52px; width: 34px; height: 34px; background: var(--frame-red); }
  .headline {
    right: 66px; top: 295px; text-align: right;
    font-family: "Changa One", "Arial Black", sans-serif; font-size: 66px; line-height: 0.92;
    color: var(--headline-red); text-shadow: 3px 3px 0 var(--headline-shadow);
  }
  .intro { left: 30px; top: 575px; width: 560px; font-size: 13px; line-height: 17.5px; }
  .intro h2, .sidebar h3, .tagline { font-family: "Arvo", Georgia, serif; }
  .intro h2 { font-size: 20px; color: var(--plum-dark); margin-bottom: 3px; }
  .intro p { margin-bottom: 16px; }
  .benefits { list-style: none; margin: -6px 0 16px; }
  .benefits li { position: relative; padding-left: 24px; margin-bottom: 9px; }
  .benefits li.no-mark { padding-left: 24px; }
  .benefits li:not(.no-mark)::before {
    content: ""; position: absolute; left: 0; top: 2px; width: 13px; height: 13px; border-radius: 50%; background: var(--ink);
  }
  .tagline { display: block; text-align: center; color: var(--plum-dark); font-size: 17px; line-height: 20px; margin-top: -2px; }
  .partners { left: 28px; top: 1024px; width: 560px; height: 68px; }
  .partner-name { position: absolute; left: 0; top: 20px; font-size: 14px; color: var(--ink); }
  .partner-name i { display: inline-block; width: 14px; height: 14px; background: var(--frame-red); margin-right: 6px; vertical-align: -2px; }
  .badge { position: absolute; top: 4px; }
  .badge--round { left: 160px; width: 62px; height: 62px; border-radius: 50%; background: #d9d4c2; }
  .badge--oval { left: 236px; width: 56px; height: 56px; border-radius: 50%; background: #3d4f9c; }
  .badge--square { left: 300px; top: 10px; width: 58px; height: 44px; background: #5ab6e6; border-radius: 4px; }
  .sponsor { position: absolute; left: 410px; top: 0; font-size: 11px; color: #555; }
  .sponsor strong { display: block; margin-top: 10px; font-size: 22px; color: var(--frame-red); font-weight: 400; }
  .footer-bar {
    left: 6px; top: 1102px; width: 580px; height: 32px; border-radius: 16px;
    background: var(--plum-dark); color: var(--white); font-size: 11px;
    display: flex; align-items: center;
  }
  .footer-bar span { flex: 1; padding-left: 16px; display: flex; align-items: center; gap: 8px; border-right: 1px solid #a57a98; }
  .footer-bar span:last-child { border-right: 0; }
  .footer-bar b { display: inline-block; width: 14px; height: 14px; border: 1.5px solid var(--white); border-radius: 50%; }
  .sidebar { left: 602px; top: 593px; width: 278px; height: 553px; background: var(--orchid); color: var(--white); font-size: 11px; line-height: 14px; }
  .sidebar h3 { background: var(--ink); font-size: 19px; padding: 7px 16px; height: 34px; }
  .sidebar ul { list-style: none; padding: 10px 20px 12px; }
  .sidebar li { position: relative; padding-left: 20px; margin-bottom: 5px; }
  .sidebar li::before { content: ""; position: absolute; left: 0; top: 2px; width: 10px; height: 10px; border-radius: 50%; background: var(--ink); }
  .sidebar p { padding: 10px 20px 0; text-align: justify; }
  .sidebar p + h3 { margin-top: 12px; }
  .sidebar .spaced { margin-top: 0; }
</style>
</head>
<body>
<div class="flyer">
  <div class="flyer__inner"></div>
  <div class="flyer__sheet">
    <div class="sheet-abs hero-photo" role="img" aria-label="Photo of two women walking along a rocky beach by the sea"></div>
    <svg class="sheet-abs chevron" viewBox="0 0 880 620" aria-hidden="true">
      <polygon points="0,431 464,540 880,431 880,461 464,570 0,461" fill="#4e1640"/>
      <polygon points="0,461 464,570 880,461 880,473 464,582 0,473" fill="#8d2f72"/>
      <polygon points="0,473 464,582 880,473 880,620 0,620" fill="#ffffff"/>
      <polygon points="602,546 880,473 880,620 602,620" fill="#b94c9e"/>
    </svg>
    <div class="sheet-abs brand-banner">
      <svg width="387" height="178" viewBox="0 0 387 178" aria-hidden="true">
        <polygon points="0,0 387,0 387,140 193,178 0,140" fill="#ffffff" stroke="#7c2763" stroke-width="2"/>
      </svg>
      <span class="brand-banner__dot"></span>
      <span class="brand-banner__name">MX Bridge</span>
    </div>
    <div class="sheet-abs headline">Join<br>mxbridge.org<br>today!</div>

    <section class="sheet-abs intro">
      <h2>Get Connected.</h2>
      <p>One of the most important steps towards finding effective treatments for lipodystrophy (LD) is to uncover the ways in which the diseases behave, the symptoms that are commonly seen and how those symptoms progress. This requires the collection of as much information as possible about all people affected by LD. MX Bridge will serve as that database–the critical link between the patient community and the scientific community. The more people who join the registry the greater the chances that research will produce results that benefit everyone.</p>
      <p>Join THE CONNECT RTQV Registry to:</p>
      <ul class="benefits">
        <li>Tell us about your experience with LD and learn about the experiences with others</li>
        <li class="no-mark">Share information in a program that protects your privacy</li>
        <li>Provide valuable quality-of-life information that can be used to advocate on behalf of the LD community</li>
        <li>Help the research community launch clinical trials and studies</li>
      </ul>
      <p>We need to hear YOUR VOICE and we hope you will decide to join MX Bridge. Every individual who joins makes a vital contribution toward helping all of those affected by lipodystrophy.</p>
      <strong class="tagline">Your information will lead to future treatments<br>and cures for all types of Lipodystrophy</strong>
    </section>

    <div class="sheet-abs partners">
      <span class="partner-name"><i></i>Allied Patients United</span>
      <span class="badge badge--round"></span>
      <span class="badge badge--oval"></span>
      <span class="badge badge--square"></span>
      <div class="sponsor">Sponsored by:<strong>Norvale Pharma</strong></div>
    </div>

    <div class="sheet-abs footer-bar">
      <span><b></b>www.RTQVRegistry.org</span>
      <span><b></b>info@patientjunction.com</span>
      <span><b></b>Copyright © 2014 PatientJunction</span>
    </div>

    <aside class="sheet-abs sidebar">
      <h3>Who Can Participate</h3>
      <ul>
        <li>Patients</li>
        <li>Family members</li>
        <li>Healthcare providers</li>
        <li>Investigators &amp; researchers</li>
        <li>All stakeholders interested in RTQV</li>
      </ul>
      <h3 class="spaced">How it Works</h3>
      <p>Patients can join the registry to submit their data. After taking web-based surveys, explore the collected information in a way that protects the privacy of everyone.</p>
      <h3>Who We Are</h3>
      <p>As its name implies, MX Bridge represents the coming together of a wide range of entities and individuals who recognize the value in pooling their combined expertise and information. The Governing Board of MX Bridge comes from leaders in the non-profit sector, government agencies and academic institutions.</p>
      <p>Regardless of their individual backgrounds, the thought leaders of MX Bridge share a common goal to increase the community's ability to help one another through improved communication, and by doing so, to help the millions of people affected by Lipodystrophy.</p>
    </aside>
  </div>
</div>
</body>
</html>
```